Thornwell Building Company - advertisement poster

I am looking to print some canvas signs to advertise my general contracting company, Thornwell Building Company. The sign will measure 6' long x 3' high so the size should match that ratio. I already have a logo icon, which is the Letter 'A' and some trees that I would like to incorporate, see attached. I would also like the to have the following information listed:
1) phone number: 472-318-6095
2) email: thornwellbuildingcompany@mailvistra.net
3) website: thornwellbuildingcompany.com
4) Lic#5386204
5) I want to use this text: "BUILD WITH THE T-CREW!"

The ad should be relatively simple and clean. Black and Green are my company colors. I am open to creative ideas!

Target Market(s)

People looking to renovate their homes

Industry/Entity Type

Construction

Colors
59FF00
82FF00
B8FF75
E3FFCB
F4FFEA

Requirements
Must have
• Must have my company logo
Should not have
• No photos or complex graphics

```html
<!DOCTYPE html>
<html lang="en">
<head>
<meta charset="utf-8">
<title>Thornwell Building Company – Sign</title>
<link href="https://fonts.googleapis.com/css2?family=Poppins:wght@400;500;600;700;800&display=swap" rel="stylesheet">
<style>
  :root{
    --page:#cfcfcf;
    --ink:#141414;
    --ink-soft:#262626;
    --green:#5cb847;
    --green-bright:#6cc94f;
    --white:#ffffff;
    --muted:#d9d9d9;
    --house-sky:#4a5fa8;
    --house-warm:#c79a5c;
    --kitchen-wood:#8a5a36;
    --kitchen-light:#d8d4cc;
    --bath-stone:#8c8c88;
    --glass-dark:#1d2622;
  }
  *{margin:0;padding:0;box-sizing:border-box}
  html,body{width:1200px;height:1200px;overflow:hidden;background:var(--page)}
  body{font-family:"Poppins",sans-serif;position:relative}
  .sign{
    position:absolute;left:50px;top:325px;width:1100px;height:550px;
    background:var(--ink);overflow:hidden;
  }
  .interior-backdrop{
    position:absolute;inset:0;
    background:radial-gradient(ellipse at 45% 65%, #3a3a38 0%, #262625 40%, #141414 85%);
  }
  .photo-panels{position:absolute;inset:0;width:1100px;height:550px}
  .brand{
    position:absolute;left:61px;top:74px;display:flex;align-items:center;gap:10px;
  }
  .brand-square{width:14px;height:14px;background:var(--green)}
  .brand-name{
    color:var(--white);font-weight:600;font-size:15px;letter-spacing:1.5px;line-height:1.25;
    text-transform:uppercase;
  }
  .headline{
    position:absolute;left:58px;top:152px;
    color:var(--white);font-weight:700;font-size:78px;line-height:70px;letter-spacing:-0.5px;
  }
  .headline .accent{color:var(--green-bright)}
  .book-btn{
    position:absolute;left:222px;top:327px;width:172px;height:40px;border-radius:20px;
    background:var(--green);color:var(--white);font-weight:500;font-size:17px;
    display:flex;align-items:center;justify-content:center;
  }
  .contacts{position:absolute;left:60px;top:392px;list-style:none}
  .contacts li{display:flex;align-items:center;gap:7px;height:27px;color:var(--white);font-size:12.5px;font-weight:500}
  .contacts li.email{font-weight:400;color:var(--muted)}
  .contacts svg{width:14px;height:14px;flex:none}
  .license{
    position:absolute;left:171px;top:488px;font-size:24px;font-weight:600;display:flex;gap:30px;
  }
  .license .label{color:var(--green-bright)}
  .license .number{color:var(--white)}
</style>
</head>
<body>
<main class="sign">
  <div class="interior-backdrop" role="img" aria-label="Dimmed photo of a modern living room with a sectional sofa"></div>

  <svg class="photo-panels" viewBox="0 0 1100 550" aria-hidden="false">
    <defs>
      <linearGradient id="houseGrad" x1="0" y1="0" x2="0" y2="1">
        <stop offset="0" stop-color="var(--house-sky)"/>
        <stop offset="1" stop-color="var(--house-warm)"/>
      </linearGradient>
      <linearGradient id="kitchenGrad" x1="0" y1="0" x2="0" y2="1">
        <stop offset="0" stop-color="var(--kitchen-wood)"/>
        <stop offset="1" stop-color="var(--kitchen-light)"/>
      </linearGradient>
      <linearGradient id="bathGrad" x1="0" y1="0" x2="0" y2="1">
        <stop offset="0" stop-color="var(--bath-stone)"/>
        <stop offset="1" stop-color="#d6d6d2"/>
      </linearGradient>
    </defs>
    <polygon points="860,0 1100,0 1100,270 1030,270" fill="var(--glass-dark)" role="img" aria-label="Photo of dark glass wall with trees"/>
    <polygon points="564,0 826,0 686,251" fill="url(#houseGrad)" role="img" aria-label="Photo of a lit modern two-storey house at dusk"/>
    <polygon points="838,6 698,251 1016,251" fill="url(#houseGrad)" role="img" aria-label="Photo of the same modern house continued"/>
    <polygon points="686,267 1009,267 856,550 826,550" fill="url(#kitchenGrad)" role="img" aria-label="Photo of a modern kitchen with wood ceiling"/>
    <polygon points="1024,274 861,550 1100,550 1100,274" fill="url(#bathGrad)" role="img" aria-label="Photo of a bathroom with a freestanding tub"/>
  </svg>

  <div class="brand">
    <span class="brand-square"></span>
    <span class="brand-name">Thornwell<br>Building Company</span>
  </div>

  <h1 class="headline">BUILD WITH<br>THE <span class="accent">T-CREW</span></h1>

  <div class="book-btn">BOOK NOW</div>

  <ul class="contacts">
    <li class="phone">
      <svg viewBox="0 0 16 16"><circle cx="8" cy="8" r="7" fill="none" stroke="var(--green)" stroke-width="1.3"/><path d="M5.5 4.5l1.3 0 .6 1.8-.8.7a5 5 0 0 0 2.4 2.4l.7-.8 1.8.6v1.3c-3.6.3-6.3-2.4-6-6z" fill="var(--green)"/></svg>
      472-318-6095
    </li>
    <li class="web">
      <svg viewBox="0 0 16 16"><circle cx="8" cy="8" r="7" fill="none" stroke="var(--green)" stroke-width="1.3"/><circle cx="8" cy="8" r="4" fill="none" stroke="var(--green)" stroke-width="1"/><path d="M4 8h8M8 4v8" stroke="var(--green)" stroke-width="1"/></svg>
      thornwellbuildingcompany.com
    </li>
    <li class="email">
      <svg viewBox="0 0 16 16"><circle cx="8" cy="8" r="7" fill="none" stroke="var(--green)" stroke-width="1.3"/><rect x="4.5" y="5.5" width="7" height="5" fill="var(--green)"/><path d="M4.5 5.5l3.5 2.8 3.5-2.8" fill="none" stroke="var(--ink)" stroke-width=".8"/></svg>
      thornwellbuildingcompany@mailvistra.net
    </li>
  </ul>

  <div class="license"><span class="label">license</span><span class="number">#5386204</span></div>
</main>
</body>
</html>
```